Clinc flyer

We need a flyer for our Physiotherapy and Acupuncture clinic to leave in a gym.
It needs the clinc logo and also:
"Free physiotherapy and acupuncture treament with an LPB claim." This should be larger text
"No referral needed" This should be under the previous text
"271c Tarevo Mall (entry via Brindle St)"
"582 3910"

```html
<!DOCTYPE html>
<html lang="en">
<head>
<meta charset="utf-8">
<title>Kinetra Health – Clinic Flyer</title>
<link rel="stylesheet" href="https://fonts.googleapis.com/css2?family=Oswald:wght@600;700&family=Open+Sans:wght@400;600&display=swap">
<style>
  :root {
    --sky: #27aee3;
    --teal: #0e6280;
    --teal-deep: #0a4a63;
    --ink: #1e1e1e;
    --paper: #ffffff;
    --mist: #e9ecef;
  }
  * { margin: 0; padding: 0; box-sizing: border-box; }
  html, body { width: 848px; height: 1200px; overflow: hidden; background: #fff; }
  .flyer {
    position: relative;
    width: 848px;
    height: 1200px;
    overflow: hidden;
    background: linear-gradient(180deg, var(--paper) 0%, var(--paper) 45%, var(--mist) 100%);
    font-family: "Open Sans", sans-serif;
  }
  .brand {
    position: absolute;
    top: 29px;
    left: 184px;
    display: flex;
    align-items: center;
    gap: 26px;
  }
  .brand-dot {
    width: 70px; height: 70px;
    border-radius: 50%;
    background: var(--teal);
  }
  .brand-text { display: flex; flex-direction: column; }
  .brand-name {
    font-weight: 600;
    font-size: 54px;
    line-height: 58px;
    color: var(--sky);
    letter-spacing: -0.5px;
  }
  .brand-tagline {
    font-weight: 400;
    font-size: 14px;
    line-height: 16px;
    letter-spacing: 6.6px;
    color: var(--teal);
    margin-top: 1px;
    padding-left: 2px;
  }
  .hero-art { position: absolute; top: 0; left: 0; }
  .free-badge {
    position: absolute;
    left: 41px; top: 507px;
    width: 246px; height: 246px;
    border-radius: 50%;
    background: radial-gradient(circle at 50% 35%, #1b86a8 0%, var(--teal) 55%, var(--teal-deep) 100%);
    border: 8px solid var(--sky);
    box-shadow: 0 0 0 6px #fff, 0 4px 10px rgba(0,0,0,.25);
    display: flex; align-items: center; justify-content: center;
  }
  .free-badge span {
    font-family: "Oswald", sans-serif;
    font-weight: 700;
    font-size: 86px;
    color: #fff;
    letter-spacing: 1px;
    text-shadow: 0 3px 4px rgba(0,0,0,.35);
  }
  .offer { position: absolute; left: 300px; top: 672px; }
  .offer-line {
    font-family: "Oswald", sans-serif;
    font-weight: 700;
    font-size: 62px;
    line-height: 76px;
    letter-spacing: 0.5px;
  }
  .offer-line.primary { color: var(--sky); }
  .offer-line.secondary { color: var(--teal); }
  .offer-note {
    font-weight: 600;
    font-size: 35px;
    color: var(--ink);
    margin-top: 2px;
  }
  .no-referral {
    position: absolute;
    left: 457px; top: 898px;
    width: 349px; height: 53px;
    background: var(--sky);
    color: #fff;
    font-size: 33px;
    display: flex; align-items: center; justify-content: center;
  }
  .call {
    position: absolute;
    left: 358px; top: 1000px;
    width: 448px; height: 71px;
    border-radius: 36px 4px 4px 36px;
    background: linear-gradient(180deg, #177d9f 0%, var(--teal-deep) 100%);
    display: flex; align-items: center;
  }
  .call-icon {
    width: 71px; height: 71px;
    border-radius: 50%;
    background: #fff;
    border: 4px solid var(--teal);
    display: flex; align-items: center; justify-content: center;
  }
  .call-text {
    font-family: "Oswald", sans-serif;
    font-weight: 700;
    font-size: 52px;
    color: #fff;
    margin-left: 14px;
    letter-spacing: 0.5px;
  }
  .care-photo {
    position: absolute;
    left: 6px; top: 880px;
    width: 330px; height: 254px;
    background: linear-gradient(180deg, #eceef0 0%, #e2e5e8 100%);
  }
  .address-band { position: absolute; left: 0; bottom: 0; }
  .address {
    position: absolute;
    left: 0; bottom: 14px; width: 848px;
    text-align: center;
    color: #fff;
    font-weight: 600;
    font-size: 25px;
  }
</style>
</head>
<body>
<main class="flyer">
  <div class="brand">
    <div class="brand-dot"></div>
    <div class="brand-text">
      <div class="brand-name">Kinetra Health</div>
      <div class="brand-tagline">ACUPUNCTURE PHYSIOTHERAPY</div>
    </div>
  </div>

  <svg class="hero-art" width="848" height="700" viewBox="0 0 848 700">
    <defs>
      <linearGradient id="heroPhoto" x1="0" y1="0" x2="1" y2="1">
        <stop offset="0" stop-color="#f1f3f5"/>
        <stop offset="0.55" stop-color="#dde3e8"/>
        <stop offset="1" stop-color="#b7d4e8"/>
      </linearGradient>
    </defs>
    <path d="M0 410 Q 380 660 848 460 L848 490 Q 390 700 0 440 Z" fill="#bfe6f6"/>
    <path d="M0 430 Q 390 690 848 475 L848 500 Q 400 720 0 460 Z" fill="#1d7fa6"/>
    <path role="img" aria-label="Photo: physiotherapist taping a patient's knee in a treatment room"
          d="M6 110 L848 110 L848 430 Q 380 640 6 405 Z" fill="url(#heroPhoto)"/>
    <path d="M0 405 Q 380 640 848 430 L848 455 Q 380 670 0 430 Z" fill="var(--sky)"/>
  </svg>

  <div class="free-badge"><span>FREE</span></div>

  <section class="offer">
    <div class="offer-line primary">PHYSIOTHERAPY</div>
    <div class="offer-line secondary">&amp; ACUPUNCTURE</div>
    <div class="offer-note">Treament with an LPB claim</div>
  </section>

  <div class="no-referral">No referral needed</div>

  <div class="call">
    <div class="call-icon">
      <svg width="36" height="40" viewBox="0 0 24 24">
        <path fill="#0e6280" d="M6.6 10.8c1.4 2.8 3.8 5.1 6.6 6.6l2.2-2.2c.3-.3.7-.4 1-.2 1.1.4 2.3.6 3.6.6.6 0 1 .4 1 1V20c0 .6-.4 1-1 1C10.6 21 3 13.4 3 4c0-.6.4-1 1-1h3.5c.6 0 1 .4 1 1 0 1.3.2 2.5.6 3.6.1.3 0 .7-.2 1z"/>
      </svg>
    </div>
    <div class="call-text">CALL: 582 3910</div>
  </div>

  <div class="care-photo" role="img" aria-label="Photo: therapist treating a woman's neck and shoulder"></div>

  <svg class="address-band" width="848" height="68" viewBox="0 0 848 68">
    <defs>
      <linearGradient id="bandFill" x1="0" y1="0" x2="0" y2="1">
        <stop offset="0" stop-color="#157899"/>
        <stop offset="1" stop-color="#0a4a63"/>
      </linearGradient>
    </defs>
    <path d="M0 68 L0 12 Q 60 0 120 0 L728 0 Q 800 0 848 18 L848 68 Z" fill="url(#bandFill)"/>
  </svg>
  <div class="address">Address: 271c Tarevo Mall (entry via Brindle St)</div>
</main>
</body>
</html>
```